Rise As Captain Book Cover Design

Book Cover Design Brief
Book Title
Rise As Captain
Subtitle
The 10 Quiet Habits of Remarkable Command
Author
Orwen Dalquist
Overview
This book is about leadership that starts within.
Most leadership books focus on tactics or management strategies. This book focuses on the inner disciplines that create powerful leaders — mindset, integrity, focus, empathy, professionalism, honesty, and self-respect.
The tone of the book is bold, direct, confident, and transformational.
This is not a soft or corporate leadership book. It is a call to step up and become the leader you are capable of becoming.
The cover should feel:
• Powerful
• Professional
• Transformational
• Premium
• Memorable
Think best-selling leadership book, not a generic business book.
Target Audience
Business owners
Managers
Entrepreneurs
Team leaders
Professionals who want to grow as leaders
Most readers are ambitious professionals who want to level up their leadership and life.
Design Direction
The design should communicate:
Strength. Discipline. Leadership. Personal transformation.
Avoid cliché leadership visuals like:
• Handshakes
• Office buildings
• Corporate stock imagery
• Teams sitting around tables
The design should feel iconic, bold, and timeless.
Think about covers of successful leadership books such as:
Copper Rituals
Total Stewardship
Won't Break Now
Begin From Purpose
The 36 Rules of Sway
These covers are simple, powerful, and recognizable even at small sizes.
Typography
The title RISE AS CAPTAIN should be:
• Bold
• Strong
• Dominant on the cover
• Easy to read even at small sizes (important for Vellora thumbnails)
The subtitle should be clean and secondary to the title.
The overall typography should feel strong, modern, and premium.
Color Direction
Designers are free to explore colors, but the cover should feel strong and premium, not playful.
Colors that often work well for leadership books include:
Black
Gold
White
Deep blue
Dark red
High contrast and clarity are important.
Style
Preferred style:
• Clean
• Modern
• Minimal
• Strong contrast
Avoid clutter and overly busy designs.
The goal is to create a cover that feels powerful and professional at first glance.
Deliverables
Front cover design for a leadership book.
Final files should include:
• High resolution artwork
• Editable source files
• Print-ready version suitable for publishing
Goal of the Cover
When someone sees this book on Vellora or in a bookstore, they should immediately think:
“This looks like a serious leadership book.”
The design should feel like it belongs next to books by authors such as:
Marcus Thorley
Brandt Osgood
Peter Hollis
Nolan Fairbrook
A strong, confident cover that attracts leaders who want to grow and perform at a higher level.
Target Market(s)
Business Owners and High level managers
Look and feel
Each slider illustrates characteristics of the customer's brand and the style your logo design should communicate.

```html
<!DOCTYPE html>
<html lang="en">
<head>
<meta charset="utf-8">
<title>Rise As Captain — Book Cover</title>
<link rel="stylesheet" href="https://fonts.googleapis.com/css2?family=Bebas+Neue&family=Montserrat:wght@500&display=swap">
<style>
  :root {
    --page: #ffffff;
    --cover-black: #000000;
    --title-red: #ed2124;
    --subtitle-white: #ffffff;
    --author-ink: #000000;
  }
  html, body {
    margin: 0;
    padding: 0;
    width: 1200px;
    height: 1200px;
    overflow: hidden;
    background: var(--page);
  }
  .canvas {
    position: relative;
    width: 1200px;
    height: 1200px;
    background: var(--page);
  }
  .cover {
    position: absolute;
    left: 250px;
    top: 72px;
    width: 708px;
    height: 1063px;
    background: var(--cover-black);
    overflow: hidden;
  }
  .cover-title {
    position: absolute;
    left: 0;
    top: 0;
    width: 708px;
    height: 700px;
  }
  .cover-title text {
    font-family: 'Bebas Neue', 'Oswald', sans-serif;
    font-size: 262px;
    fill: var(--title-red);
  }
  .cover-subtitle {
    position: absolute;
    left: 0;
    top: 715px;
    width: 708px;
    margin: 0;
    text-align: center;
    font-family: 'Montserrat', sans-serif;
    font-weight: 500;
    font-size: 33px;
    line-height: 48px;
    color: var(--subtitle-white);
  }
  .author-band {
    position: absolute;
    left: 0;
    bottom: 0;
    width: 708px;
    height: 102px;
    background: var(--title-red);
    display: flex;
    align-items: center;
    justify-content: center;
  }
  .author-name {
    font-family: 'Bebas Neue', 'Oswald', sans-serif;
    font-size: 80px;
    line-height: 1;
    letter-spacing: 0.1em;
    color: var(--author-ink);
    padding-top: 8px;
    margin-right: -0.1em;
  }
</style>
</head>
<body>
  <main class="canvas">
    <section class="cover" aria-label="Book cover: Rise As Captain by Orwen Dalquist">
      <svg class="cover-title" viewBox="0 0 708 700" aria-label="Rise As Captain" role="heading">
        <text x="354" y="239" text-anchor="middle">RISE</text>
        <text x="354" y="456" text-anchor="middle">AS</text>
        <text x="354" y="675" text-anchor="middle">CAPTAIN</text>
      </svg>
      <p class="cover-subtitle">The 10 Quiet Habits of<br>Remarkable Command</p>
      <div class="author-band">
        <span class="author-name">Orwen Dalquist</span>
      </div>
    </section>
  </main>
</body>
</html>
```